Package/Product Design: Fullora 100% Scalp Coverage Powders

Need to design "high style" box and product disc design. Open to any and all suggestions. We sell 800+ skus a month on Marketvale and looking to take our box design to the next level so that we can sell even more with new look. Our competition is https://www.brevano.com/ and https://www.quillsy.com/ I know Brevano has a ton of money,,, but their products look "high touch, high style" and that is what we are going after. The compact has to have the ingredients on the back, same as the box. So looking for a design that makes the packaging look sleek, and still gets out point across. Logo should be in White or Black.

Target Market(s)

We sell to individuals who are experiencing hair loss, thinning hair, or gray/balding hair. This product creates the illusion of hair and allows clients get gain back confidence.

We sell on Marketvale (search fullora or scalp concealer), and www.fullorahairdust.com

Industry/Entity Type

Hair And Beauty

Logo Text

Fullora 100% Scalp Coverage Powders

Colors

Designer to choose colors to be used in the design.

Requirements
Must have
• Quality/high touch/high feel look to the packaging. Open to any and all suggestions.

```html
<!DOCTYPE html>
<html lang="en">
<head>
<meta charset="utf-8">
<title>Fullora Hair Powder – Box Dieline</title>
<link rel="stylesheet" href="https://fonts.googleapis.com/css2?family=Open+Sans:wght@400;700&family=Cousine:wght@400;700&family=Oswald:wght@500&display=swap">
<style>
  :root {
    --canvas: #d3d3d3;
    --black: #050505;
    --panel-dark: #1d1d1f;
    --panel-mid: #2a2a2c;
    --gold: #f2b632;
    --gold-light: #fff3b8;
    --gold-deep: #a8701a;
    --ink: #111111;
    --white: #ffffff;
    --badge-edge: #c9c9c9;
  }
  html, body { margin: 0; padding: 0; overflow: hidden; background: var(--canvas); }
  .dieline { display: block; width: 1200px; height: 1050px; }
  .flap { fill: var(--black); }
  .body-text { font-family: "Open Sans", sans-serif; }
  .mono { font-family: "Cousine", monospace; }
  .badge-text { font-family: "Oswald", sans-serif; font-weight: 500; fill: var(--white); font-size: 13px; text-anchor: middle; }
  .brand-name { font-family: "Open Sans", sans-serif; font-weight: 700; }
  .gold-fill { fill: var(--gold); }
  .white-fill { fill: var(--white); }
  .gold-frame { fill: none; stroke: var(--gold); stroke-width: 2; }
</style>
</head>
<body>
<svg class="dieline" viewBox="0 0 1500 1313" xmlns="http://www.w3.org/2000/svg">
  <defs>
    <linearGradient id="goldSheen" x1="0" y1="0" x2="1" y2="0">
      <stop offset="0" stop-color="#b97f1f"/>
      <stop offset="0.3" stop-color="#f2c452"/>
      <stop offset="0.5" stop-color="#fff6c8"/>
      <stop offset="0.7" stop-color="#f0bf48"/>
      <stop offset="1" stop-color="#a36a17"/>
    </linearGradient>
    <linearGradient id="darkPanel" x1="0" y1="0" x2="1" y2="1">
      <stop offset="0" stop-color="#2b2b2d"/>
      <stop offset="0.5" stop-color="#1c1c1e"/>
      <stop offset="1" stop-color="#262628"/>
    </linearGradient>
    <radialGradient id="badgeFill" cx="0.5" cy="0.35" r="0.7">
      <stop offset="0" stop-color="#4a4a4a"/>
      <stop offset="1" stop-color="#141414"/>
    </radialGradient>
  </defs>

  <!-- flaps -->
  <polygon class="flap" points="15,350 135,330 135,795 15,775"/>
  <polygon class="flap" points="135,330 205,218 275,218 342,330"/>
  <polygon class="flap" points="135,795 342,795 275,908 205,908"/>
  <polygon class="flap" points="812,330 878,218 950,218 1018,330"/>
  <polygon class="flap" points="812,795 1018,795 950,908 878,908"/>
  <polygon class="flap" points="352,795 812,795 812,1060 800,1112 352,1112"/>
  <path class="flap" d="M1025,120 L1040,13 L1470,13 L1485,120 L1485,330 L1025,330 Z"/>

  <!-- lid: brand upside down -->
  <g class="lid-brand" transform="translate(1255,215) rotate(180)">
    <text class="brand-name gold-fill" x="0" y="0" font-size="40" text-anchor="middle">FULLORA</text>
    <text class="mono gold-fill" x="0" y="20" font-size="14" text-anchor="middle" letter-spacing="2">100% Scalp Coverage</text>
  </g>

  <!-- left side panel: directions -->
  <rect x="135" y="330" width="207" height="465" fill="url(#darkPanel)" role="img" aria-label="Dark geometric triangle pattern background"/>
  <rect class="gold-frame" x="167" y="348" width="113" height="430"/>
  <g class="body-text" transform="translate(270,362) rotate(90)" font-size="15">
    <text class="gold-fill" font-weight="700" x="0" y="0">Directions:</text>
    <text class="gold-fill" x="0" y="22">In a circular motion, rub applicator brush around the</text>
    <text class="gold-fill" x="0" y="43">pressed powder. Lightly apply to desired area directly</text>
    <text class="gold-fill" x="0" y="64">on the scalp using small round strokes. Repeat until</text>
    <text class="gold-fill" x="0" y="85">proper coverage is obtained.</text>
  </g>
  <g transform="translate(302,560) rotate(90)">
    <text class="brand-name gold-fill" x="0" y="0" font-size="26" text-anchor="middle">FULLORA</text>
    <text class="mono gold-fill" x="0" y="12" font-size="9" text-anchor="middle" letter-spacing="1.5">100% Scalp Coverage</text>
  </g>
  <text class="mono gold-fill" transform="translate(148,565) rotate(90)" font-size="13" text-anchor="middle">HAIR POWDER | TALC-FREE</text>

  <!-- front panel -->
  <rect x="342" y="330" width="470" height="465" fill="url(#goldSheen)"/>
  <path d="M342,630 Q577,800 812,630 L812,795 L342,795 Z" fill="var(--black)"/>
  <text class="brand-name" x="567" y="445" font-size="62" text-anchor="middle" fill="var(--ink)" letter-spacing="1">FULLORA</text>
  <text class="mono" x="575" y="472" font-size="22" text-anchor="middle" fill="var(--ink)" letter-spacing="4">100% Scalp Coverage</text>
  <g class="shade-dots" stroke="#6a4a1a" stroke-width="2">
    <circle cx="487" cy="518" r="11" fill="#8a6a45"/>
    <circle cx="535" cy="518" r="11" fill="#6b4526"/>
    <circle cx="583" cy="518" r="11" fill="#4e3623"/>
    <circle cx="631" cy="518" r="11" fill="#1c1a19"/>
    <circle cx="680" cy="518" r="11" fill="#7a4a22"/>
  </g>
  <rect x="425" y="562" width="310" height="48" fill="none" stroke="#2a2014" stroke-width="1.5"/>
  <text class="mono" x="580" y="596" font-size="28" text-anchor="middle" fill="var(--ink)" letter-spacing="8">HAIR POWDER</text>
  <line x1="580" y1="610" x2="580" y2="632" stroke="#2a2014" stroke-width="1.5"/>
  <text class="mono" x="580" y="658" font-size="24" text-anchor="middle" fill="var(--ink)" letter-spacing="1">TALC-FREE</text>
  <g class="claim-badges">
    <circle cx="457" cy="712" r="43" fill="url(#badgeFill)" stroke="var(--badge-edge)" stroke-width="2"/>
    <text class="badge-text" x="457" y="700">100%</text>
    <text class="badge-text" x="457" y="715">INSTANT</text>
    <text class="badge-text" x="457" y="730">COVERAGE</text>
    <circle cx="575" cy="712" r="43" fill="url(#badgeFill)" stroke="var(--badge-edge)" stroke-width="2"/>
    <text class="badge-text" x="575" y="708">FILLSIN</text>
    <text class="badge-text" x="575" y="723">BALD SPOTS</text>
    <circle cx="700" cy="712" r="43" fill="url(#badgeFill)" stroke="var(--badge-edge)" stroke-width="2"/>
    <text class="badge-text" x="700" y="708">WATERPROOF</text>
    <text class="badge-text" x="700" y="723">EASY TO APPLY</text>
  </g>
  <text class="mono white-fill" x="575" y="778" font-size="16" text-anchor="middle">Net Wt.32OZ/9G</text>

  <!-- right side panel: ingredients -->
  <rect x="812" y="330" width="206" height="465" fill="url(#darkPanel)" role="img" aria-label="Dark geometric triangle pattern background"/>
  <rect class="gold-frame" x="866" y="343" width="121" height="439"/>
  <g class="body-text gold-fill" transform="translate(886,772) rotate(-90)" font-size="13">
    <text x="0" y="0" font-weight="700">Ingredients:</text>
    <text x="0" y="15">Mica, Kaolin, Octyldodecyl Stearoyl Stearate, Synthetic Wax,</text>
    <text x="0" y="30">Ethylhexyl Palmitate, Bis-Diglyceryl Polyacyladipate-2, Tocopheryl</text>
    <text x="0" y="45">Acetate, Phenoxyethanol, Methylparaben, Propylparaben, Caprylyl</text>
    <text x="0" y="60">Glycol, Ethylhexylglycerin, CI 77891, CI 77492, CI 77499,</text>
    <text x="0" y="75">CI 77491</text>
    <text x="0" y="90">LOT: 12122013-01</text>
  </g>
  <g transform="translate(838,560) rotate(-90)">
    <text class="brand-name gold-fill" x="0" y="0" font-size="26" text-anchor="middle">FULLORA</text>
    <text class="mono gold-fill" x="0" y="14" font-size="9" text-anchor="middle" letter-spacing="1.5">100% Scalp Coverage</text>
  </g>

  <!-- back panel -->
  <rect x="1018" y="330" width="467" height="465" fill="url(#darkPanel)" role="img" aria-label="Dark geometric triangle pattern background"/>
  <g class="body-text">
    <text class="gold-fill" x="1253" y="380" font-size="17" font-weight="700" text-anchor="middle">Fullora 100% Scalp Coverage Benefits:</text>
    <g class="white-fill" font-size="15" text-anchor="middle">
      <text x="1253" y="403">100% scalp coverage fills in balding or thinning spots</text>
      <text x="1253" y="421">and looks like natural growing hair. Great for those</text>
      <text x="1253" y="439">in-between color weeks or also to use on cowlicks</text>
      <text x="1253" y="457">which causes separation on the hair. Available in five</text>
      <text x="1253" y="475">colors which will blend well with any color hair or mix</text>
      <text x="1253" y="493">two colors together to achieve a blended color look</text>
      <text x="1253" y="511">for highlighted or even salt and pepper hair. Fullora</text>
      <text x="1253" y="529">100% Scalp Coverage is water insoluble and</text>
      <text x="1253" y="547">TALC-FREE.</text>
    </g>
    <text class="gold-fill" x="1253" y="569" font-size="17" font-weight="700" text-anchor="middle">WARNING:</text>
    <text class="white-fill" x="1253" y="591" font-size="17" text-anchor="middle">Keep out of eyes. Stop use if irritation occurs.</text>
    <text class="white-fill" x="1253" y="612" font-size="17" text-anchor="middle">Keep out of reach of children.</text>
    <text class="brand-name gold-fill" x="1253" y="655" font-size="32" text-anchor="middle">FULLORA</text>
    <text class="mono gold-fill" x="1255" y="667" font-size="10" text-anchor="middle" letter-spacing="2">100% Scalp Coverage</text>
    <text class="gold-fill" x="1253" y="697" font-size="17" font-weight="700" text-anchor="middle">Fullora Hair Powder</text>
    <text class="white-fill" x="1253" y="713" font-size="13" text-anchor="middle">2840 Linden Ct STE 12B</text>
    <text class="white-fill" x="1253" y="729" font-size="13" text-anchor="middle">Maple Ridge, FL 33190</text>
    <text class="gold-fill" x="1253" y="744" font-size="13" font-weight="700" text-anchor="middle">www.fullorahairdust.com</text>
    <text class="white-fill" x="1253" y="774" font-size="13" text-anchor="middle">Made in PR.C.</text>
  </g>
  <g class="period-after-opening" fill="none" stroke="var(--white)" stroke-width="2">
    <path d="M1380,750 L1380,772 L1420,772 L1420,750 Z"/>
    <path d="M1378,742 L1418,722 L1422,730 L1382,750"/>
    <text x="1400" y="768" font-size="12" text-anchor="middle" fill="var(--white)" stroke="none" class="body-text">24M</text>
  </g>
</svg>
</body>
</html>
```